We are an Estate agency (Real estate)– looking for Christmas/winter theme leaflet

We are called ‘’HOLLWICKS’’ we are an estate agency based in England. We opened in 2020 in February, few weeks before Covid and we are now known as one of the fastest growing agencies in all of Brighton and Hove.
This is our first Christmas/winter leaflet and this kind of offer!
Offer is: if the client signs with us to sell their home from 1st December 2021 until 7th January 2022 they will receive 50% off HOLLWICKS fees.
I am looking for A5 two-sided leaflet. The first side should contain our branding, the offer. Also, maybe this: ‘’ Let us Treat you this Christmas’’ or maybe on the other side of leaflet, which will contain explanation of the offer, our office details etc. the back should also contain some design.
Our target market is higher end clients who own a property in Brighton and Hove and looking to sell. I would say target market 35+ years of age.
Our branding is clean, fresh and eye catching and that’s what leaflet should look like and represent.
I will insert our website link so you could have a look at the properties that we deal with too. I could also insert last leaflet which I designed and had a really positive response & feedback… maybe will give you some ideas.
I have inserted our brand guidelines. We use Hollwicks in white or blue backgrounds as in guideline.
https://www.hollwicksestateagents.co.uk/
Hi guys,
Thank you for all your ideas so far, however just wanted to mention that I am looking for not so much ''in your face Christmas'' design - something subtle.
Needs to be classy, modern and eye catching - our target market is property owners 35+ years of age. Moreover, this offer needs to be perceived as one off opportunity.
35+ property owners

```html
<!DOCTYPE html>
<html lang="en">
<head>
<meta charset="utf-8">
<title>Hollwicks Christmas Leaflet</title>
<link rel="stylesheet" href="https://fonts.googleapis.com/css2?family=Baloo+2:wght@400;700;800&family=Ubuntu:wght@400;500;700&display=swap">
<style>
  :root {
    --navy: #062742;
    --magenta: #d90b8a;
    --white: #ffffff;
    --sky-light: #eef4f8;
    --sky-blue: #7ec8ea;
    --backdrop: #ececee;
  }
  * { margin: 0; padding: 0; box-sizing: border-box; }
  html, body { width: 1200px; height: 958px; overflow: hidden; background: var(--backdrop); }
  .canvas { position: relative; width: 1200px; height: 958px; }

  .leaflet { position: absolute; top: 122px; width: 497px; height: 705px; overflow: hidden; }
  .leaflet--front { left: 85px; }
  .leaflet--back { left: 621px; background: var(--navy); }

  .photo-area {
    position: absolute; inset: 0;
    background: linear-gradient(160deg, var(--sky-light) 0%, #d7e9f3 45%, var(--sky-blue) 100%);
  }
  .sign-area {
    position: absolute; left: 165px; top: 30px; width: 360px; height: 240px;
    background: linear-gradient(145deg, #3a2a3e 0%, #1d1b2a 60%, #b81a75 100%);
    transform: rotate(-15deg);
    border-radius: 4px;
  }
  .band { position: absolute; inset: 0; width: 100%; height: 100%; }

  .hanger { position: absolute; top: 0; width: 0; border-left: 2px dotted var(--magenta); }
  .leaflet--front .hanger { left: 76px; height: 115px; }
  .leaflet--back .hanger { left: 69px; height: 110px; }

  .headline {
    position: absolute; left: 0; right: 0; top: 372px;
    font-family: "Baloo 2", sans-serif; font-weight: 800; color: var(--navy);
    text-align: center; line-height: 0.98; letter-spacing: -1px;
  }
  .headline__line { display: block; font-size: 56px; }
  .headline__line--big { font-size: 78px; margin-top: 2px; }

  .brand { position: absolute; left: 0; right: 0; top: 34px; text-align: center; }
  .brand__square { display: block; margin: 0 auto 22px; width: 68px; height: 86px; border: 4px solid var(--magenta); }
  .brand__name {
    font-family: "Ubuntu", sans-serif; font-weight: 500; font-size: 24px;
    letter-spacing: 6px; color: var(--white); padding-left: 6px;
  }

  .offer { position: absolute; left: 0; right: 0; top: 270px; font-family: "Baloo 2", sans-serif; color: var(--navy); }
  .offer__get { position: absolute; left: 83px; top: 0; font-size: 44px; font-weight: 800; line-height: 1; }
  .offer__number { position: absolute; left: 154px; top: -16px; font-size: 152px; font-weight: 800; line-height: 1; letter-spacing: -6px; }
  .offer__percent { position: absolute; left: 326px; top: 0; font-size: 80px; font-weight: 800; line-height: 1; }
  .offer__off { position: absolute; left: 322px; top: 76px; font-size: 38px; font-weight: 800; line-height: 1; }
  .offer__fees { position: absolute; left: 0; right: 0; top: 120px; text-align: center; font-size: 42px; line-height: 1; letter-spacing: -0.5px; }
  .offer__fees strong { font-weight: 800; }
  .offer__fees span { font-weight: 400; }
  .offer__terms {
    position: absolute; left: 0; right: 0; top: 176px; text-align: center;
    font-family: "Ubuntu", sans-serif; font-size: 14.5px; line-height: 1.4; color: var(--white);
  }
  .offer__terms sup { font-size: 8px; }

  .contact { position: absolute; left: 0; right: 0; top: 584px; text-align: center; font-family: "Ubuntu", sans-serif; }
  .contact__row { display: flex; align-items: center; justify-content: center; gap: 7px; }
  .contact__phone { font-size: 35px; font-weight: 500; color: var(--white); letter-spacing: 0.5px; }
  .contact__address { margin-top: 6px; font-size: 16px; font-weight: 500; color: var(--white); }
  .contact__web { margin-top: 6px; font-size: 15.5px; font-weight: 500; color: var(--magenta); }
  .icon { display: block; flex: none; }
</style>
</head>
<body>
<main class="canvas">

  <section class="leaflet leaflet--front" aria-label="Leaflet front">
    <div class="photo-area" role="img" aria-label="Photograph of the agency's pink shop sign against a blue, cloudy sky"></div>
    <div class="sign-area" role="img" aria-label="Shop sign in the photograph"></div>
    <svg class="band" viewBox="0 0 497 705" preserveAspectRatio="none" aria-hidden="true">
      <polygon points="0,376 497,276 497,584 0,684" fill="var(--magenta)"/>
    </svg>
    <span class="hanger" aria-hidden="true"></span>
    <h1 class="headline">
      <span class="headline__line">Let us Treat</span>
      <span class="headline__line">you this</span>
      <span class="headline__line headline__line--big">Christmas!</span>
    </h1>
  </section>

  <section class="leaflet leaflet--back" aria-label="Leaflet back">
    <svg class="band" viewBox="0 0 497 705" preserveAspectRatio="none" aria-hidden="true">
      <polygon points="0,273 497,171 497,481 0,580" fill="var(--magenta)"/>
    </svg>
    <span class="hanger" aria-hidden="true"></span>

    <header class="brand">
      <span class="brand__square" aria-hidden="true"></span>
      <p class="brand__name">HOLLWICKS</p>
    </header>

    <div class="offer">
      <span class="offer__get">Get</span>
      <span class="offer__number">50</span>
      <span class="offer__percent">%</span>
      <span class="offer__off">OFF</span>
      <p class="offer__fees"><strong>HOLLWICKS</strong> <span>FEES</span></p>
      <p class="offer__terms">when you sign with us to sell your home<br>from 1<sup>st</sup> December 2021 until 7<sup>th</sup> January 2022</p>
    </div>

    <footer class="contact">
      <p class="contact__row contact__phone">
        <svg class="icon" width="32" height="32" viewBox="0 0 32 32" aria-hidden="true">
          <circle cx="16" cy="16" r="14" fill="none" stroke="var(--white)" stroke-width="2.4"/>
          <path d="M11 9.5c1-.8 2-.6 2.5.3l1.4 2.6c.4.8.1 1.5-.6 2l-.9.7c.8 1.8 2.2 3.3 4 4.2l.8-.9c.6-.6 1.3-.8 2-.4l2.5 1.5c.8.5 1 1.6.2 2.5-1.3 1.5-3.1 1.7-5 .7-3.6-1.9-6.2-4.8-7.5-8.4-.6-1.8-.4-3.5.6-4.8z" fill="none" stroke="var(--white)" stroke-width="2"/>
        </svg>
        01273 555018
      </p>
      <p class="contact__row contact__address">
        <svg class="icon" width="12" height="17" viewBox="0 0 12 17" aria-hidden="true">
          <path d="M6 1a5 5 0 0 1 5 5c0 3.5-5 9-5 9S1 9.5 1 6a5 5 0 0 1 5-5z" fill="none" stroke="var(--white)" stroke-width="2"/>
          <circle cx="6" cy="6" r="1.8" fill="var(--white)"/>
        </svg>
        48 Elm Parade, Hove, BN3 7QX
      </p>
      <p class="contact__row contact__web">
        <svg class="icon" width="15" height="15" viewBox="0 0 16 16" aria-hidden="true">
          <circle cx="8" cy="8" r="6.8" fill="none" stroke="var(--magenta)" stroke-width="1.5"/>
          <ellipse cx="8" cy="8" rx="3" ry="6.8" fill="none" stroke="var(--magenta)" stroke-width="1.3"/>
          <path d="M1.5 6h13M1.5 10h13" stroke="var(--magenta)" stroke-width="1.3"/>
        </svg>
        www.hollwicksestateagents.co.uk
      </p>
    </footer>
  </section>

</main>
</body>
</html>
```